Brambleway Business Card

I have a business that is called "Brambleway Electrical Goods LTD" My company deals with top of the range laptops and mobile phones that are exclusive. I need a business card that will be eye catching but not over complicated.

Target Market(s)

Adults aged 19 to 50
Upper middle class

Industry/Entity Type

Business

Requirements
Must have
• Company name/logo (file attached)
• It must have my contact information which is:

• Name: Dale Margrove

• Position: Managing Director 

• Business Address: 7 Haddon Row, London, W4 9QZ

• Contact Number: 02085519304
• Mobile: 07815206473
• Email: info@brambleway-goods.co.uk
Nice to have
• Simple and stylish
• Eye catching

```html
<!DOCTYPE html>
<html lang="en">
<head>
<meta charset="utf-8">
<title>Brambleway Electrical Goods – Business Card</title>
<link href="https://fonts.googleapis.com/css2?family=Arimo:ital,wght@0,400;0,700;1,400&display=swap" rel="stylesheet">
<style>
  :root {
    --edge-grey: #808080;
    --card-white: #ffffff;
    --panel-blue: #7fc5e3;
    --ink: #1c1c1c;
    --brand-blue: #1a8cc0;
  }
  html, body {
    margin: 0;
    padding: 0;
    width: 1200px;
    height: 733px;
    overflow: hidden;
    background: var(--card-white);
  }
  .card {
    position: relative;
    width: 1200px;
    height: 733px;
    background: var(--card-white);
    font-family: "Arimo", Arial, sans-serif;
    color: var(--ink);
  }
  .edge-strip {
    position: absolute;
    left: 0;
    top: 0;
    width: 55px;
    height: 100%;
    background: var(--edge-grey);
  }
  .brand {
    position: absolute;
    left: 55px;
    top: 0;
    width: 675px;
    height: 100%;
  }
  .brand-dot {
    position: absolute;
    left: 50%;
    top: 150px;
    width: 170px;
    height: 170px;
    margin-left: -85px;
  }
  .brand-name {
    position: absolute;
    left: 0;
    width: 100%;
    text-align: center;
    color: var(--brand-blue);
    font-weight: 400;
    margin: 0;
  }
  .brand-name--main {
    top: 400px;
    font-size: 64px;
    line-height: 1;
    letter-spacing: 1px;
  }
  .brand-name--sub {
    top: 492px;
    font-size: 29px;
    line-height: 1;
    letter-spacing: 2px;
  }
  .details {
    position: absolute;
    left: 730px;
    top: 0;
    width: 470px;
    height: 100%;
    background: var(--panel-blue);
  }
  .details p {
    position: absolute;
    left: 29px;
    margin: 0;
    white-space: nowrap;
    line-height: 1;
  }
  .person-name {
    top: 72px;
    font-size: 39px;
    font-weight: 700;
  }
  .person-role {
    top: 138px;
    font-size: 33px;
    font-style: italic;
  }
  .address {
    top: 360px;
    font-size: 29px;
    line-height: 37px !important;
  }
  .phone-office { top: 508px; font-size: 29px; }
  .phone-mobile { top: 561px; font-size: 29px; }
  .email { top: 613px; font-size: 29px; }
</style>
</head>
<body>
  <div class="card">
    <div class="edge-strip"></div>

    <div class="brand">
      <svg class="brand-dot" viewBox="0 0 170 170" aria-hidden="true">
        <circle cx="85" cy="85" r="85" fill="var(--brand-blue)"/>
      </svg>
      <p class="brand-name brand-name--main">Brambleway</p>
      <p class="brand-name brand-name--sub">Electrical Goods</p>
    </div>

    <div class="details">
      <p class="person-name">Dale Margrove</p>
      <p class="person-role">Managing Director</p>
      <p class="address">7, Haddon Row,<br>London, W4 9QZ</p>
      <p class="phone-office">02085519304</p>
      <p class="phone-mobile">07815206473</p>
      <p class="email">info@brambleway-goods.co.uk</p>
    </div>
  </div>
</body>
</html>
```